Brochure for Charter Boat

We require a brochure for a new charter boat business, called Tidewell Reef Cruises, We do Fishing Charters, Pellmont Isle Nature Trips, Diving, and Whale Watching tour.

Pellmont Isle Nature Trips - Lighthouse, seals.

We offer refreshments on all our charters and lunch is provided on a full day fishing charter.

We are waiting on photos. but have included some photos, I can change photos later. Would like to put a photo of the boat in, but still waiting to receive it from photographer.

www.tidewellreefcruises.example (currently changing website, just purchased design from artbazaar).

Reason: getting a logo designed by artbazaar, so I can add logo to brochure. Thank you!

Reason: As I haven't provided information and now have a logo which was desinged by ArtBazaar.

Target Market(s)

Fisherman and Families

Industry/Entity Type

Business

Requirements
Must have
• Phone number, website, business Name - Tidewell Reef Cruises and logo. Please include 'specalising in Small Groups'

Photo of boat, (which I'm waiting on at the moment)
Nice to have
• 1/2 Day fishing $150 per person - 5 hours, refreshments provided. Includes all fishing tackle & bait.
Full Day Fishing $250 per person - 9 hours, Lunch and refreshments provided. Includes all fishing tackle & bait
2 Hour Fish - $80 per person, drinks provided and all fishing tackle & bait
4 hour Morning Pellmont Nature Trip - $120 per person, refreshments provided
3 hour Afternoon Pellmont Nature Trip - $100 per person, refreshments provided.
Vessel: 9.8 meter custom built plate aluminium.
Whale watching from September to November

```html
<!DOCTYPE html>
<html lang="en">
<head>
<meta charset="utf-8">
<title>Tidewell Reef Cruises – Brochure Inside Spread</title>
<link rel="stylesheet" href="https://fonts.googleapis.com/css2?family=Noto+Sans:wght@400&display=swap">
<style>
  :root {
    --lime: #d3e02c;
    --ocean: #1b7fae;
    --panel: #c4d6e4;
    --ink-blue: #2378a6;
    --ink-dark: #1b2b45;
  }
  html, body {
    margin: 0;
    padding: 0;
    width: 1200px;
    height: 928px;
    overflow: hidden;
    background: #ffffff;
  }
  .brochure {
    position: relative;
    width: 1200px;
    height: 928px;
    overflow: hidden;
    font-family: "Noto Sans", Verdana, sans-serif;
  }
  .frame { position: absolute; inset: 0; }
  .panel {
    position: absolute;
    left: 15px;
    top: 15px;
    width: 1170px;
    height: 898px;
    background: var(--panel);
  }
  .photo { position: absolute; }
  .photo--divers {
    left: 944px;
    top: 15px;
    width: 241px;
    height: 175px;
    background: radial-gradient(ellipse at 55% 45%, rgba(159,195,216,0.85), rgba(196,214,228,0) 75%);
  }
  .photo--catch {
    left: 40px;
    top: 700px;
    width: 372px;
    height: 213px;
    background: radial-gradient(ellipse at 45% 55%, rgba(201,211,220,0.95), rgba(170,198,216,0.6) 55%, rgba(196,214,228,0) 85%);
  }
  .copy {
    position: absolute;
    margin: 0;
    color: var(--ink-blue);
    font-size: 28.5px;
    line-height: 36.4px;
    white-space: nowrap;
  }
  .copy p { margin: 0 0 36.4px; }
  .copy span { display: block; }
  .copy--left { left: 47px; top: 93px; }
  .copy--right { left: 853px; top: 204px; }
  .brand {
    position: absolute;
    left: 396px;
    top: 732px;
    width: 400px;
    display: flex;
    align-items: center;
    justify-content: center;
    gap: 10px;
  }
  .brand__dot {
    width: 28px;
    height: 28px;
    border-radius: 50%;
    background: var(--ocean);
  }
  .brand__name {
    color: var(--ocean);
    font-size: 26px;
    line-height: 36px;
    white-space: nowrap;
  }
  .contact {
    position: absolute;
    left: 346px;
    top: 831px;
    width: 500px;
    text-align: center;
    color: var(--ink-dark);
    font-size: 20px;
    line-height: 25px;
  }
  .contact p { margin: 0; }
</style>
</head>
<body>
<div class="brochure">
  <svg class="frame" width="1200" height="928" viewBox="0 0 1200 928" aria-hidden="true">
    <rect width="1200" height="928" fill="var(--lime)"/>
    <rect x="230" y="0" width="244" height="15" fill="var(--ocean)"/>
    <rect x="722" y="0" width="242" height="15" fill="var(--ocean)"/>
    <rect x="230" y="913" width="244" height="15" fill="var(--ocean)"/>
    <rect x="722" y="913" width="242" height="15" fill="var(--ocean)"/>
    <rect x="0" y="194" width="15" height="178" fill="var(--ocean)"/>
    <rect x="0" y="556" width="15" height="178" fill="var(--ocean)"/>
    <rect x="1185" y="194" width="15" height="178" fill="var(--ocean)"/>
    <rect x="1185" y="556" width="15" height="178" fill="var(--ocean)"/>
  </svg>

  <div class="panel"></div>

  <div class="photo photo--divers" role="img" aria-label="Faded photo of divers underwater"></div>
  <div class="photo photo--catch" role="img" aria-label="Faded photo of a fishing group on the boat holding their catch"></div>

  <div class="copy copy--left">
    <p>
      <span>Tidewell Reef Cruises</span>
      <span>specialising in</span>
      <span>Small Groups.</span>
      <span>Fishing charters,</span>
      <span>nature trips, diving</span>
      <span>and whale watching.</span>
      <span>Refreshments on</span>
      <span>all our charters.</span>
    </p>
    <p>
      <span>1/2 Day Fishing</span>
      <span>$150 pp, 5 hours.</span>
      <span>Full Day Fishing</span>
      <span>$250 pp, 9 hours,</span>
      <span>lunch provided.</span>
    </p>
    <p>
      <span>2 Hour Fish $80 pp.</span>
      <span>All tackle &amp; bait</span>
      <span>included.</span>
    </p>
  </div>

  <div class="copy copy--right">
    <p>
      <span>Pellmont Isle</span>
      <span>Nature Trips:</span>
      <span>lighthouse, seals</span>
      <span>and island views.</span>
      <span>4 hour morning trip</span>
      <span>$120 per person.</span>
      <span>3 hour afternoon</span>
      <span>trip, $100 pp.</span>
    </p>
    <p>
      <span>Whale watching</span>
      <span>September to</span>
      <span>November.</span>
      <span>Refreshments</span>
      <span>provided.</span>
    </p>
    <p>
      <span>Vessel: 9.8 m custom</span>
      <span>built plate</span>
      <span>aluminium.</span>
    </p>
  </div>

  <div class="brand">
    <span class="brand__dot"></span>
    <span class="brand__name">Tidewell Reef Cruises</span>
  </div>

  <div class="contact">
    <p>Wharf Road, Pellmont Bay</p>
    <p>Phone (02) 5550 1847</p>
    <p>www.tidewellreefcruises.example</p>
  </div>
</div>
</body>
</html>
```